Brochure Design Project for Home Watch company

We are a new start up company in fast growing home watch industry. We provide services in Hawaii so the design needs to be reflect that. Our web site can give you overview of what we do - www.breezekeepcare.com. We will service clients that own second homes in Hawaii. These properties are not necessarily income producing properties for our clients. I'm looking for 2 or 4 page brochure which will be used to market our services to potential new clients. It needs to be high quality, modern with slight Hawaiian feel (we are based on Oahu). I'm not looking for a trifold type of brochure.

We are open to various colors based on what the designer might suggest but as you can see on our home page - the main picture of the home on our site has lots of red and white which we like as well as the "head" or dot above the "i" in our logo is red. I was not able to upload the file of the main house (purchased on snapmeadow) on here therefore I'll have to provide the original photo to the selected designer at the later time. For now I just uploaded the not purchased copy.

If you have other questions please do let me know. And lastly, I will be looking to create a business card and post card as well.

```html
<!DOCTYPE html>
<html lang="en">
<head>
<meta charset="utf-8">
<title>Breeze Keep Care – Brochure Spread</title>
<link href="https://fonts.googleapis.com/css2?family=Lato:wght@300;400;700&display=swap" rel="stylesheet">
<style>
  :root {
    --red: #ef4f4f;
    --ink: #2b2b2b;
    --body: #333333;
    --page: #ffffff;
    --page-alt: #f5f5f5;
    --icon-bg: #e6e6e6;
    --line: #dcdcdc;
  }
  * { margin: 0; padding: 0; box-sizing: border-box; }
  html, body { width: 1200px; height: 830px; overflow: hidden; background: #e4e4e2; }
  body { font-family: "Lato", sans-serif; color: var(--body); }
  .spread { position: relative; width: 1200px; height: 830px; display: flex; }
  .page { position: relative; width: 600px; height: 830px; overflow: hidden; }
  .page--left { background: var(--page); }
  .page--right { background: var(--page-alt); }
  .abs { position: absolute; }
  .hero { left: 0; top: 0; width: 600px; height: 250px;
    background: linear-gradient(180deg, #5f7fb6 0%, #8da3c6 35%, #6f7d52 60%, #3f8fb0 80%, #2f6a8a 100%); }
  .hero-wave { left: 0; top: 190px; width: 600px; height: 70px; }
  .heading { font-weight: 300; color: var(--ink); text-align: center; }
  .text { font-size: 9.6px; line-height: 12.2px; text-align: justify; }
  .h-main { left: 0; width: 600px; top: 274px; font-size: 16px; }
  .intro-1 { left: 53px; width: 515px; top: 302px; }
  .intro-2 { left: 53px; width: 515px; top: 408px; }
  .kicker { left: 0; width: 600px; top: 533px; font-size: 9.5px; text-align: center; color: #555; }
  .section-title { font-weight: 400; color: var(--red); text-align: center; }
  .primary { left: 0; width: 600px; top: 545px; font-size: 21px; }
  .h-sub { font-size: 14.5px; }
  .col-a { left: 39px; width: 250px; }
  .col-b { left: 316px; width: 250px; }
  .h-row { top: 586px; }
  .t-row { top: 605px; text-align: left; }
  .h-interior { left: 0; width: 600px; top: 679px; }
  .t-interior { left: 39px; width: 522px; top: 699px; text-align: left; }

  .concierge { left: 0; width: 600px; top: 38px; font-size: 21px; }
  .col-pre { left: 40px; width: 243px; }
  .col-post { left: 318px; width: 243px; }
  .h-row2 { top: 84px; font-size: 14.5px; }
  .t-row2 { top: 103px; }
  .h-special { left: 0; width: 600px; top: 244px; font-size: 14.5px; }
  .t-special { left: 40px; width: 521px; top: 263px; }
  .value { width: 150px; text-align: center; top: 385px; }
  .value-badge { width: 52px; height: 52px; border-radius: 50%; background: var(--icon-bg);
    margin: 0 auto 8px; display: flex; align-items: center; justify-content: center; }
  .value-label { font-size: 11px; line-height: 13.5px; color: #444; }
  .quote-box { left: 39px; top: 496px; width: 508px; height: 202px; border: 1.5px solid var(--line);
    border-radius: 20px; background: #fff; }
  .quote-mark { color: var(--red); font-size: 18px; font-weight: 700; position: absolute; }
  .quote-text { left: 32px; top: 36px; width: 232px; font-size: 10.8px; line-height: 14.2px; color: #444; }
  .house-art { left: 272px; top: 6px; width: 230px; height: 188px; border-radius: 12px;
    background: linear-gradient(180deg, #f3f3f3, #d9d9d9); }
  .bottom-wave { left: 0; top: 690px; width: 600px; height: 100px; }
  .url { right: 50px; top: 776px; font-size: 14.5px; color: var(--red); letter-spacing: .3px; }
</style>
</head>
<body>
<main class="spread">
  <section class="page page--left">
    <div class="abs hero" role="img" aria-label="Photo of a tropical vacation home at dusk with a lit pool, palm trees and mountains"></div>
    <svg class="abs hero-wave" viewBox="0 0 600 70" preserveAspectRatio="none">
      <path d="M0 70 L0 60 C160 78 330 52 600 34 L600 70 Z" fill="var(--red)"/>
      <path d="M0 70 L0 66 C170 84 340 62 600 58 L600 70 Z" fill="var(--page)"/>
    </svg>

    <h1 class="abs heading h-main">We’re Keeping a Close Eye on Your Home!</h1>
    <p class="abs text intro-1">Breeze Keep Care provides necessary services for absentee owners of vacation/second homes as well as local residents traveling for extended periods of time. We provide our clients with three of the most precious commodities – peace of mind, time and convenience. We protect their investment and do more than just watch their home in their absence. We take care of the problems while they are gone so they can relax and enjoy their home when they return. We are accredited by Coastal Home Care Alliance which only grants accreditation to companies that meet criteria for insurance and bonding and are in good standing with customers and organizations such as Fair Trade Council and agree to abide by the association’s code of ethics and mission statement.</p>
    <p class="abs text intro-2">Home Watch is a visual inspection of a vacant home or a vacation rental property on a regular basis where we look for obvious issues and report our findings to you, the client. Our clients determine the frequency of home checks – weekly, bi-weekly, monthly. We verify and track our visits using TrackVisit Home Watch Software that uses GPS positioning to provide evidence that a visit was made. TrackVisit is FREE to our clients and provides instant real time reporting. If needed, and upon the client’s request, we solicit estimates for any required service(s) from contractors and other vendors, submit for our client’s review and approval and further coordinate and oversee the work being done on the property. Our standard and additional/concierge services are described below:</p>

    <p class="abs kicker">Monthly, bi-weekly or weekly visual inspections</p>
    <h2 class="abs section-title primary">Primary HOME WATCH</h2>

    <h3 class="abs heading h-sub col-a h-row">General Outdoor Visual Inspections</h3>
    <p class="abs text col-a t-row">Check yard, lawn and landscaping; check lanai, deck, and pool area for any damage; check for mold or fading of all outdoor furniture; check water level of swimming pool or hot tub, if applicable</p>
    <h3 class="abs heading h-sub col-b h-row">Home Exterior Visual Inspections</h3>
    <p class="abs text col-b t-row">Check security cameras; check for overall damage; remove mail, newspapers, and flyers from mailbox and store inside of the property; check outdoor plumbing and hoses for leakage; check garage; check for vandalism and theft</p>

    <h3 class="abs heading h-sub h-interior">Home Interior Visual Inspections</h3>
    <p class="abs text t-interior">Make sure security system is in working order; ensure that all doors, windows and sliders are locked and secured; check thermostats and make sure the air conditioning is set at appropriate and requested temperature; make sure all smoke detectors are in proper working order or replace batteries if necessary; visually inspect the water heater and washer and dryer</p>
  </section>

  <section class="page page--right">
    <h2 class="abs section-title concierge">Concierge Services</h2>
    <h3 class="abs heading col-pre h-row2">Pre-Arrival</h3>
    <p class="abs text col-pre t-row2">Groceries purchased and stored, air conditioning and ceiling vents turned on and/or windows opened, water turned on, flowers placed, fresh laundered linens on beds, towels arranged in the bathrooms, deck furniture placed on decks and patio, house freshened up and aired out, security system disarmed as appropriate, decks, walkways, lanais, and driveways cleaned of debris and special requests completed.</p>
    <h3 class="abs heading col-post h-row2">Post-Departure</h3>
    <p class="abs text col-post t-row2">House cleaning coordinated, beds made, sheets and towels cleaned, dishes washed and put away, all doors and windows secured, lights on timers set, water turned off, outdoor furniture stored or covered per specific instructions, driveways, lanais, walkways and decks cleared of debris, air conditioning set to appropriate level, trash placed for collection and security system turned on.</p>

    <h3 class="abs heading h-special">Sample of Special Services/Requests</h3>
    <p class="abs text t-special">Key holding services, mail forwarding, coordination of transportation from and to the airport, light handyman and landscaping services, vendor coordination (we coordinate access and meet everyone you authorize at your home including but not limited to maintenance, repair, pest control, landscaping and tree trimming, and utility providers), pre-storm services (secure outdoor furniture, potted plants, hammocks and any other outdoor items, etc.) and post-storm services (clean walkway and driveway, pick-up trash, etc.), and emergency services response, etc. Additional services and pricing available upon request.</p>

    <div class="abs value" style="left:78px">
      <div class="value-badge">
        <svg width="30" height="22" viewBox="0 0 30 22"><path d="M1 8 L8 2 L15 6 L22 2 L29 8 L22 16 L17 20 L13 17 L8 14 Z" fill="none" stroke="var(--red)" stroke-width="2.4" stroke-linejoin="round"/><path d="M11 9 L16 13 M14 7 L19 11" stroke="var(--red)" stroke-width="2"/></svg>
      </div>
      <p class="value-label">High moral and ethical values</p>
    </div>
    <div class="abs value" style="left:223px">
      <div class="value-badge">
        <svg width="24" height="22" viewBox="0 0 24 22"><path d="M12 21 L2 11 C-2 6 3 -1 8 2 C10 3 11 4 12 6 C13 4 14 3 16 2 C21 -1 26 6 22 11 Z" fill="var(--red)"/></svg>
      </div>
      <p class="value-label">Passionate and hardworking attitude</p>
    </div>
    <div class="abs value" style="left:368px">
      <div class="value-badge">
        <svg width="26" height="26" viewBox="0 0 26 26"><path d="M3 8 H9 A3.5 3.5 0 1 1 15 8 H21 V13 A3.5 3.5 0 1 1 21 19 V24 H3 Z" fill="var(--red)"/></svg>
      </div>
      <p class="value-label">Enhanced attention to details</p>
    </div>

    <div class="abs quote-box">
      <span class="quote-mark" style="left:14px;top:32px">“</span>
      <p class="abs quote-text">Put your mind at ease and let us keep your real estate investment maintained at the level you expect with our detailed monthly, bimonthly or weekly home watch services. Don’t come home to discover water leak, broken air conditioning unit, leaking showerheads, pest and insects infestation, mold and mildew, nonfunctioning fridge and many more other issues that might arise during your absence. <span style="color:var(--red);font-weight:700">”</span></p>
      <div class="abs house-art" role="img" aria-label="Cutaway illustration of a house with rooms, garage and palm trees, ringed by round service icons"></div>
    </div>

    <svg class="abs bottom-wave" viewBox="0 0 600 100" preserveAspectRatio="none">
      <path d="M20 72 C200 96 380 40 600 25 L600 56 C400 50 220 92 20 72 Z" fill="var(--red)"/>
    </svg>
    <p class="abs url">www.BreezeKeepCare.com</p>
  </section>
</main>
</body>
</html>
```